Ich möchte den bisher erstellten Flyer (habe ich hochgeladen) ein wnig 'umstylen', mit dem neuen Logo. Der 200 Euro Bonus sol als Geldschein dargestellt werden.

```html
<!DOCTYPE html>
<html lang="de">
<head>
<meta charset="utf-8">
<title>Juravia Lounge – Flyer</title>
<link href="https://fonts.googleapis.com/css2?family=Ubuntu:wght@300;400;700&display=swap" rel="stylesheet">
<style>
  :root {
    --backdrop: #e6e6e6;
    --page-black: #151515;
    --gold: #d6ad57;
    --gold-light: #ecd293;
    --gold-dark: #a9822f;
    --ink: #1c1a14;
    --photo-light: #dfe3e8;
    --photo-mid: #8e9aa8;
    --photo-dark: #2e3440;
  }
  * { margin: 0; padding: 0; box-sizing: border-box; }
  html, body {
    width: 1200px; height: 921px; overflow: hidden;
    background: var(--backdrop);
    font-family: "Ubuntu", sans-serif;
  }
  .spread {
    position: absolute; left: 60px; top: 60px;
    width: 1080px; height: 800px;
    display: flex;
  }
  .page {
    position: relative;
    width: 540px; height: 800px;
    background: var(--page-black);
    color: var(--gold);
    text-align: center;
  }
  .page--back { border-right: 1px solid #262626; }

  /* back page */
  .back-claim {
    position: absolute; top: 215px; left: 0; right: 0;
    font-size: 28px; font-weight: 700; line-height: 1.25;
  }
  .divider {
    position: absolute; top: 345px; left: 230px;
    width: 80px; height: 2px; background: var(--gold);
  }
  .contact {
    position: absolute; top: 372px; left: 0; right: 0;
    font-size: 14px; line-height: 1.5;
  }
  .contact-lines { margin-bottom: 12px; }
  .contact-row {
    display: flex; justify-content: center; align-items: center;
    gap: 10px; margin-top: 8px; font-size: 15px;
  }
  .contact-row svg { width: 16px; height: 16px; fill: none; stroke: var(--gold); stroke-width: 1.6; }
  .back-brand {
    position: absolute; top: 640px; left: 0; right: 0;
    font-size: 44px; font-weight: 300; line-height: 1.1;
  }

  /* front page */
  .hero { position: absolute; top: 0; left: 0; width: 540px; height: 300px; }
  .brand { position: absolute; top: 312px; left: 0; right: 0; }
  .brand-name { font-size: 36px; font-weight: 300; letter-spacing: 1px; line-height: 1.15; }
  .brand-tag { font-size: 14px; font-weight: 400; letter-spacing: 2px; margin-top: 4px; }
  .headline {
    position: absolute; top: 392px; left: 0; right: 0;
    font-size: 33px; font-weight: 700; line-height: 1.15;
  }
  .subline {
    position: absolute; top: 476px; left: 0; right: 0;
    font-size: 21px; font-weight: 700; line-height: 1.3;
  }
  .bonus-note {
    position: absolute; top: 546px; left: 140px;
    width: 260px; height: 116px;
  }
  .bonus-amount { font-family: "Ubuntu", sans-serif; font-weight: 700; font-size: 40px; fill: var(--ink); }
  .bonus-label { font-family: "Ubuntu", sans-serif; font-weight: 700; font-size: 13px; letter-spacing: 3px; fill: var(--ink); }
  .bonus-corner { font-family: "Ubuntu", sans-serif; font-weight: 700; font-size: 14px; fill: var(--ink); }
  .body-copy {
    position: absolute; top: 684px; left: 40px; right: 40px;
    font-size: 16.5px; font-weight: 400; line-height: 1.4;
  }
</style>
</head>
<body>
  <main class="spread">
    <section class="page page--back">
      <h2 class="back-claim">Das Juravia Lounge<br>verbindet Fortbildung,<br>Spezialwissen</h2>
      <span class="divider"></span>
      <div class="contact">
        <p class="contact-lines">Tobias Wendmark<br>Rechtsanwaltskanzlei Falkenrat<br>Lindenweg 14<br>30159 Hannover</p>
        <p class="contact-row">
          <svg viewBox="0 0 16 16"><path d="M3 2l3 1 1 3-2 1a8 8 0 0 0 4 4l1-2 3 1 1 3-2 1C7 14 2 9 2 4z" fill="#d6ad57" stroke="none"/></svg>
          +49 (0) 511 472 90 18
        </p>
        <p class="contact-row">
          <svg viewBox="0 0 16 16"><rect x="2" y="6" width="12" height="8" rx="1"/><rect x="5" y="2" width="6" height="4"/></svg>
          +49 (0) 511 472 90 19
        </p>
        <p class="contact-row">
          <svg viewBox="0 0 16 16"><rect x="1.5" y="3.5" width="13" height="9"/><path d="M1.5 3.5l6.5 5 6.5-5"/></svg>
          kanzlei@falkenrat-mail.de
        </p>
      </div>
      <p class="back-brand">Juravia<br>Lounge</p>
    </section>

    <section class="page page--front">
      <svg class="hero" viewBox="0 0 540 300">
        <defs>
          <linearGradient id="photoTone" x1="0" y1="0" x2="1" y2="1">
            <stop offset="0" stop-color="#dfe3e8"/>
            <stop offset="0.5" stop-color="#8e9aa8"/>
            <stop offset="1" stop-color="#2e3440"/>
          </linearGradient>
        </defs>
        <path role="img" aria-label="Foto: Team von Anwältinnen und Anwälten im Besprechungsraum am Konferenztisch"
              d="M0 0H540V190C500 248 420 250 330 250C220 250 110 250 0 296Z" fill="url(#photoTone)"/>
        <path d="M0 296C110 250 220 250 330 250C420 250 500 248 540 190" fill="none" stroke="#d6ad57" stroke-width="5"/>
      </svg>
      <div class="brand">
        <p class="brand-name">Juravia Lounge</p>
        <p class="brand-tag">LAWYER NETWORK</p>
      </div>
      <h1 class="headline">Recht. Vernetzt.<br>Erfolgreich.</h1>
      <h2 class="subline">Das Anwaltsportal für<br>moderne Rechtsanwälte</h2>
      <svg class="bonus-note" viewBox="0 0 260 116" role="img" aria-label="Geldschein: 200 Euro Bonus">
        <defs>
          <linearGradient id="noteTone" x1="0" y1="0" x2="1" y2="1">
            <stop offset="0" stop-color="#ecd293"/>
            <stop offset="0.55" stop-color="#d6ad57"/>
            <stop offset="1" stop-color="#a9822f"/>
          </linearGradient>
        </defs>
        <rect x="1" y="1" width="258" height="114" rx="6" fill="url(#noteTone)"/>
        <rect x="9" y="9" width="242" height="98" rx="3" fill="none" stroke="#1c1a14" stroke-width="1.2" stroke-opacity="0.55"/>
        <circle cx="206" cy="58" r="30" fill="none" stroke="#1c1a14" stroke-width="1.2" stroke-opacity="0.4"/>
        <text class="bonus-corner" x="18" y="28">200</text>
        <text class="bonus-corner" x="242" y="98" text-anchor="end">200</text>
        <text class="bonus-amount" x="110" y="70" text-anchor="middle">200 €</text>
        <text class="bonus-label" x="110" y="92" text-anchor="middle">BONUS</text>
      </svg>
      <p class="body-copy">Erfüllen Sie Ihre 15 Stunden<br>Fortbildungspflicht - und bauen Sie Ihr<br>Netzwerk unter Kollegen aus</p>
    </section>
  </main>
</body>
</html>
```